Criação de Projeto Combo top of mind para Odonto
" FAZEMOS ODONTOLOGIA TRADICIONAL (ORTODONTIA, DENTISTICA, ESTETICA, CIRURGIAS IMPLANTES ATÉ CIRURGIAS DE BUCOMAXILO FACIAL E HARMONIZAÇÃO FACIAL, SERIA UMA CLINICA INTEGRADA "

```html
<!DOCTYPE html>
<html lang="pt-BR">
<head>
<meta charset="utf-8">
<title>Envelope Saco – ORIS</title>
<link href="https://fonts.googleapis.com/css2?family=Montserrat:wght@400;500;600;700&display=swap" rel="stylesheet">
<style>
  :root{
    --green:#1d5a24;
    --gold:#b99a5c;
    --paper:#ffffff;
    --stage:#e6e6e6;
    --text:#3b3b3b;
    --faint:#f2f2f2;
  }
  *{margin:0;padding:0;box-sizing:border-box}
  html,body{width:1200px;height:1200px;overflow:hidden}
  body{background:var(--stage);font-family:"Montserrat",sans-serif;position:relative}
  .title-tab{
    position:absolute;left:259px;top:0;width:677px;height:67px;
    background:var(--green);color:#fff;
    display:flex;align-items:center;justify-content:center;
    font-weight:600;font-size:27px;letter-spacing:8px;
  }
  .envelope{position:absolute;top:199px;height:857px;box-shadow:0 6px 18px rgba(0,0,0,.18);overflow:hidden}
  .envelope--front{left:84px;width:485px;background:var(--paper)}
  .envelope--back{left:607px;width:511px;background:var(--green)}
  .watermark{position:absolute;border-radius:50%}
  .envelope--front .watermark{left:190px;top:260px;width:460px;height:460px;background:var(--faint)}
  .envelope--back .watermark{left:-120px;top:200px;width:470px;height:470px;background:rgba(255,255,255,.05)}
  .flap{position:absolute;left:0;top:0}
  .flap svg{display:block}
  .brand{position:absolute;display:flex;align-items:center}
  .brand__dot{border-radius:50%;background:var(--gold);flex:none}
  .brand__text{display:flex;flex-direction:column}
  .brand__name{font-weight:500;line-height:.9}
  .brand__tagline{font-weight:600;letter-spacing:1px;line-height:1.3;text-transform:uppercase}
  .envelope--front .brand{left:168px;top:72px;gap:8px}
  .envelope--front .brand__dot{width:40px;height:40px}
  .envelope--front .brand__name{font-size:48px;color:var(--green)}
  .envelope--front .brand__tagline{font-size:8px;color:var(--gold)}
  .envelope--back .brand{left:93px;top:317px;gap:12px}
  .envelope--back .brand__dot{width:70px;height:70px}
  .envelope--back .brand__name{font-size:96px;color:#fff}
  .envelope--back .brand__tagline{font-size:14px;color:#fff}
  .contacts{position:absolute;left:36px;top:540px;list-style:none;font-size:15px;color:var(--text);font-weight:500}
  .contacts li{display:flex;align-items:flex-start;gap:10px;margin-bottom:12px;line-height:1.25}
  .contacts .icon{width:20px;height:20px;flex:none;border-radius:50%;background:var(--gold);display:flex;align-items:center;justify-content:center}
  .contacts .icon svg{width:12px;height:12px}
</style>
</head>
<body>
  <div class="title-tab">ENVELOPE SACO</div>

  <section class="envelope envelope--front">
    <div class="watermark" aria-hidden="true"></div>
    <div class="brand">
      <span class="brand__dot"></span>
      <div class="brand__text">
        <span class="brand__name">ORIS</span>
        <span class="brand__tagline">Clínica Integrada<br>de Odontologia</span>
      </div>
    </div>
    <ul class="contacts">
      <li><span class="icon"><svg viewBox="0 0 12 12"><path d="M3 1l2 2-1 1.5c.8 1.5 2 2.7 3.5 3.5L9 7l2 2-1.5 2C5 10.5 1.5 7 1 2.5z" fill="#fff"/></svg></span><span>(91) 9870-2244<br>(91) 9870-2244</span></li>
      <li><span class="icon"><svg viewBox="0 0 12 12"><rect x="1" y="3" width="10" height="7" fill="none" stroke="#fff" stroke-width="1.3"/><path d="M1 3l5 4 5-4" fill="none" stroke="#fff" stroke-width="1.3"/></svg></span><span>orisclinica@mail.com</span></li>
      <li><span class="icon"></span><span>/Oris Clínica</span></li>
      <li><span class="icon"></span><span>@Oris Clínica</span></li>
      <li><span class="icon"><svg viewBox="0 0 12 12"><path d="M6 11S2 7 2 4.5a4 4 0 0 1 8 0C10 7 6 11 6 11z" fill="#fff"/><circle cx="6" cy="4.5" r="1.4" fill="#b99a5c"/></svg></span><span>Av. Boa Vista, 820 | Centro<br>CEP: 01234-500 | Cidade/UF</span></li>
    </ul>
  </section>

  <section class="envelope envelope--back">
    <div class="watermark" aria-hidden="true"></div>
    <div class="flap">
      <svg width="511" height="170" viewBox="0 0 511 170">
        <defs>
          <linearGradient id="flapGold" x1="0" y1="0" x2="1" y2="0">
            <stop offset="0" stop-color="#a8864b"/>
            <stop offset=".5" stop-color="#e3cd98"/>
            <stop offset="1" stop-color="#b39352"/>
          </linearGradient>
        </defs>
        <path d="M0 0H511V120Q511 160 471 160H120Q10 150 0 60Z" fill="url(#flapGold)"/>
      </svg>
    </div>
    <div class="brand">
      <span class="brand__dot"></span>
      <div class="brand__text">
        <span class="brand__name">ORIS</span>
        <span class="brand__tagline">Clínica Integrada<br>de Odontologia</span>
      </div>
    </div>
  </section>
</body>
</html>
```